Clinical Hypnotherapist needs business card design

I need a business card design that gives the impression of being approachable yet professional. As a clinical hypnotherapist I need to create trust from my clients to allow me access to their inner mind to enable them to make changes and to start to live the life that they want to live. My website is www.lunarelle.com.au and I would like my business cards to reflect my website. I would like a space for appointment details on the back of the card.

```html
<!DOCTYPE html>
<html lang="en">
<head>
<meta charset="utf-8">
<title>Clara Whitfield – Clinical Hypnotherapist Business Card</title>
<link href="https://fonts.googleapis.com/css2?family=Crimson+Text&family=Open+Sans:wght@400;700&display=swap" rel="stylesheet">
<style>
  :root {
    --backdrop: #2a2a2a;
    --plum: #8d1f7d;
    --plum-deep: #7e1a70;
    --magenta: #e0147f;
    --white: #ffffff;
    --ink: #8d1f7d;
    --dots: #a04a95;
  }
  * { box-sizing: border-box; margin: 0; padding: 0; }
  html, body {
    width: 1200px; height: 944px; overflow: hidden;
    background: var(--backdrop);
  }
  .sheet {
    width: 1200px; height: 944px;
    display: flex; flex-direction: column;
    align-items: center; justify-content: center; gap: 64px;
  }
  .card {
    position: relative;
    width: 600px; height: 343px;
    overflow: hidden;
    box-shadow: 0 12px 30px rgba(0,0,0,0.5);
  }

  /* Front */
  .card--front { background: var(--plum); }
  .name-band {
    position: absolute; left: 0; right: 0; top: 84px; height: 108px;
    background: var(--magenta);
  }
  .name-band__notch {
    position: absolute; left: 336px; top: 191px;
    width: 0; height: 0;
    border-left: 9px solid transparent;
    border-right: 9px solid transparent;
    border-top: 8px solid var(--magenta);
  }
  .identity {
    position: absolute; left: 0; right: 0; top: 92px;
    text-align: center; padding-left: 70px;
    color: var(--white);
    font-family: "Crimson Text", serif;
  }
  .identity__name { font-size: 50px; font-weight: 400; line-height: 1.05; letter-spacing: 0.5px; }
  .identity__role { font-size: 24px; line-height: 1.2; letter-spacing: 0.5px; }
  .contacts {
    position: absolute; right: 40px; top: 224px;
    font-family: "Open Sans", sans-serif; font-size: 14px;
    color: var(--white); text-align: right; line-height: 1;
  }
  .contacts__row { margin-bottom: 20px; }
  .contacts__label { color: var(--magenta); font-weight: 700; margin-left: 12px; }

  /* Back */
  .card--back { background: var(--white); }
  .appointment-head {
    height: 62px; background: var(--plum);
    display: flex; align-items: center; justify-content: center;
    color: var(--white);
    font-family: "Open Sans", sans-serif; font-weight: 700;
    font-size: 19px; letter-spacing: 0.5px;
  }
  .slot { padding: 0 40px; font-family: "Open Sans", sans-serif; color: var(--ink); }
  .slot__title { text-align: center; font-size: 17px; margin: 10px 0 6px; }
  .slot__field {
    display: flex; align-items: baseline; gap: 4px;
    font-size: 15px; height: 34px; line-height: 34px;
  }
  .slot__line {
    flex: 1; border-bottom: 2px dotted var(--dots);
    height: 0; transform: translateY(-4px);
  }
</style>
</head>
<body>
<main class="sheet">

  <section class="card card--front" aria-label="Business card front">
    <div class="name-band"></div>
    <div class="name-band__notch"></div>
    <div class="identity">
      <h1 class="identity__name">Clara Whitfield</h1>
      <p class="identity__role">Clinical Hypnotherapist</p>
    </div>
    <div class="contacts">
      <p class="contacts__row"><span class="contacts__label">P:</span> 0400 316 829</p>
      <p class="contacts__row"><span class="contacts__label">E:</span> clara@lunarelle.com.au <span class="contacts__label">W:</span> www.lunarelle.com.au</p>
    </div>
  </section>

  <section class="card card--back" aria-label="Business card back">
    <header class="appointment-head">APPOINTMENT</header>
    <div class="slot">
      <p class="slot__title">Morning</p>
      <div class="slot__field"><span>Date :</span><span class="slot__line"></span></div>
      <div class="slot__field"><span>Time :</span><span class="slot__line"></span></div>
    </div>
    <div class="slot">
      <p class="slot__title">Evening</p>
      <div class="slot__field"><span>Date :</span><span class="slot__line"></span></div>
      <div class="slot__field"><span>Time :</span><span class="slot__line"></span></div>
    </div>
  </section>

</main>
</body>
</html>
```